Business card design for strategy and management consulting company. Would like to have a clean and professional business card, based on the attached logo. The company is a strategy and management consulting company focusing on sustainable business modlels based on economic, social and environmental market opportunities. Preferably the logo should be included on both sides of the design.

Industry/Entity Type

Business

Contact Information for Business Card

Håvard Lilleby, CEO/Management consultant
havard.lilleby@quarvenpartners.example
Mob: +47 948 26 317
Office: Vikfjell gate 14, pb 312 sentrum, N-0172 Oslo Norway

Requirements
Must have
• Include attached logo
Nice to have
• Would like to have the logo on both sides
Should not have
• Many colours.

```html
<!DOCTYPE html>
<html lang="en">
<head>
<meta charset="utf-8">
<title>Quarven business card</title>
<link rel="stylesheet" href="https://fonts.googleapis.com/css2?family=Lato:wght@400;700&display=swap">
<style>
  :root {
    --stage: #2b2b2b;
    --card-black: #131313;
    --paper: #f3f3f3;
    --ink: #1d1d1d;
    --accent: #e3c51b;
    --logo-white: #ececec;
  }
  * { box-sizing: border-box; margin: 0; padding: 0; }
  html, body {
    width: 1200px; height: 900px; overflow: hidden;
    background: var(--stage);
    font-family: "Lato", sans-serif;
  }
  .stage { position: relative; width: 1200px; height: 900px; }
  .card {
    position: absolute; left: 280px;
    width: 640px; height: 366px;
    border-radius: 18px; overflow: hidden;
    background: var(--card-black);
  }
  .card--back { top: 70px; }
  .card--front { top: 470px; }

  /* back side */
  .brand {
    position: absolute; color: var(--logo-white);
    font-weight: 700; letter-spacing: -1px; line-height: 1;
  }
  .card--back .brand { left: 0; right: 0; top: 128px; text-align: center; font-size: 88px; }
  .card--back .site {
    position: absolute; left: 0; right: 0; top: 238px; text-align: center;
    color: var(--accent); font-size: 17px;
  }

  /* front side */
  .card-shapes { position: absolute; inset: 0; }
  .card--front .brand { left: 390px; width: 250px; text-align: center; top: 112px; font-size: 56px; }
  .handle {
    position: absolute; right: 28px; top: 262px;
    color: var(--ink); font-size: 16px;
  }
  .person { position: absolute; left: 36px; top: 44px; }
  .person__name { color: var(--ink); font-size: 27px; font-weight: 400; }
  .person__role { color: var(--accent); font-size: 15px; margin-top: 2px; }
  .contact { position: absolute; left: 36px; top: 132px; list-style: none; }
  .contact li {
    display: flex; align-items: flex-start; gap: 10px;
    color: var(--ink); font-size: 15px; line-height: 1.3; margin-bottom: 9px;
  }
  .contact svg { flex: none; width: 16px; height: 16px; margin-top: 2px; fill: var(--accent); }
  .front-site {
    position: absolute; left: 36px; top: 298px;
    color: var(--accent); font-size: 18px;
  }
</style>
</head>
<body>
<main class="stage">

  <section class="card card--back" aria-label="Card back">
    <div class="brand">Quarven</div>
    <div class="site">quarvenpartners.example</div>
  </section>

  <section class="card card--front" aria-label="Card front">
    <svg class="card-shapes" viewBox="0 0 640 366" preserveAspectRatio="none" aria-hidden="true">
      <polygon points="0,0 292,0 470,366 0,366" fill="var(--paper)"/>
      <polygon points="300,0 318,0 498,366 480,366" fill="var(--accent)"/>
      <polygon points="318,250 640,250 640,302 343,302" fill="var(--accent)"/>
      <polygon points="0,282 429,282 457,340 0,340" fill="var(--card-black)"/>
    </svg>

    <div class="brand">Quarven</div>
    <div class="handle">/quarven</div>

    <div class="person">
      <h1 class="person__name">Håvard Lilleby</h1>
      <p class="person__role">CEO/Management consultant</p>
    </div>

    <ul class="contact">
      <li>
        <svg viewBox="0 0 16 16"><path d="M2 5c0-2 2-3 6-3s6 1 6 3v1h-3V5H5v1H2zM4 7h8l2 7H2z"/></svg>
        <span>+47 948 26 317</span>
      </li>
      <li>
        <svg viewBox="0 0 16 16"><path d="M1 3h14v10H1zM2 4l6 5 6-5v1L8 10 2 5z"/></svg>
        <span>havard.lilleby@quarvenpartners.example</span>
      </li>
      <li>
        <svg viewBox="0 0 16 16"><path d="M8 1a5 5 0 0 1 5 5c0 4-5 9-5 9S3 10 3 6a5 5 0 0 1 5-5zm0 3a2 2 0 1 0 0 4 2 2 0 0 0 0-4z"/></svg>
        <span>Vikfjell gate 14,<br>pb 312 sentrum, Oslo Norway</span>
      </li>
    </ul>

    <div class="front-site">quarvenpartners.example</div>
  </section>

</main>
</body>
</html>
```